Modern Quillby Tree Care Website

I need a website for a full service Tree Care company. The company provides tree pruning, tree removal, tree preservation, emergency services, stump grinding, and emergency tree services.

Target Market(s)

Customers that need tree services

Industry/Entity Type

Landscaping, Tree Services

Coding

Coded - Design and coding required

Number of Pages Required

5+ page

Font styles to use
Sans Serif

Requirements
Must have
• Good clean design that showcases the services the company provides.
Nice to have
• Services page; contact form, blog, home page, about page

```html
<!DOCTYPE html>
<html lang="en">
<head>
<meta charset="utf-8">
<title>Quillby Tree Care</title>
<link href="https://fonts.googleapis.com/css2?family=Michroma&family=Montserrat:wght@400;500;600;700&family=Oswald:wght@500&display=swap" rel="stylesheet">
<style>
:root{
  --green:#7dc242;
  --orange:#f7a52b;
  --blue:#1d6fc2;
  --dark:#333d3f;
  --ink:#222;
  --muted:#555;
  --card:#f4f4f4;
  --panel:rgba(92,104,104,.82);
}
*{box-sizing:border-box;margin:0;padding:0}
html,body{width:1200px;height:4785px;overflow:hidden}
body{position:relative;font-family:'Montserrat',sans-serif;color:var(--ink);background:#fff}
.abs{position:absolute}
.btn{position:absolute;display:flex;align-items:center;justify-content:center;background:var(--green);color:#fff;font-size:12px;font-weight:500}
.btn.orange{background:var(--orange);color:#222}
.btn.inline{position:static;display:inline-flex}
.title{font-family:'Michroma',sans-serif;letter-spacing:4px;color:#4d5758;font-size:30px;font-weight:400;white-space:nowrap}
.divider{position:absolute;width:80px;height:14px}
.photo{position:absolute}

/* header */
.logo{position:absolute;display:flex;align-items:center;gap:12px}
.logo .mark{width:30px;height:30px;background:var(--orange)}
.logo .name{font-weight:700;color:#4d5758;font-size:19px;line-height:1.1;letter-spacing:1px}
.nav{position:absolute;top:41px;font-size:14px;color:#222}

/* hero */
.hero{position:absolute;top:97px;left:0;width:1200px;height:520px;overflow:hidden}
.hero h1{position:absolute;left:141px;top:100px;font-family:'Oswald',sans-serif;font-weight:500;color:#fff;font-size:46px;line-height:57px;letter-spacing:.5px}
.hero p{position:absolute;left:141px;top:282px;color:#fff;font-size:21px;font-weight:500}

/* services */
.svc{position:absolute;top:909px;height:275px;width:200px;background:var(--card)}
.svc .img{height:182px}
.svc h3{font-size:19px;font-weight:500;margin:14px 0 0 16px;white-space:nowrap}
.svc p{font-size:11px;line-height:20px;margin:6px 16px 0;color:#333}
.svc a{display:block;color:var(--orange);font-size:13px;margin:8px 0 0 16px;text-decoration:underline}
.svc.active{background:#fff;border:1px solid var(--orange);height:auto;padding-bottom:14px}
.arrow{position:absolute;top:1032px;width:36px;height:36px;border-radius:50%}

.panel{position:absolute;background:var(--panel);color:#fff}
.panel h2{font-family:'Michroma',sans-serif;font-weight:400;letter-spacing:3px;font-size:28px;line-height:40px;white-space:nowrap}
.panel p{font-size:11.5px;line-height:20px}

.area-list{position:absolute;font-size:15px;line-height:40px}
.area-list li{list-style:none;display:flex;align-items:center;gap:22px}

.why-grid{display:flex;margin-top:10px}
.why-list{font-size:14.5px;line-height:35px;color:#eee}
.why-list span{display:flex;align-items:center;gap:6px;white-space:nowrap}

.blog{position:absolute;background:#fff;box-shadow:0 2px 14px rgba(0,0,0,.12)}
.blog .date{display:flex;align-items:center;gap:8px;font-size:12px}
.blog h3{font-size:16.5px;font-weight:500;line-height:24px;margin-top:12px}
.blog p{font-size:11.5px;line-height:23px;margin-top:8px;color:#333}

.field{position:absolute;left:686px;width:373px;background:#fff;font-size:11px;color:#666;padding:14px 0 0 32px}

.footnav{position:absolute;top:4652px;font-size:14px;color:#fff}
.social{position:absolute;top:4738px;width:30px;height:30px;border:1.5px solid #ddd;border-radius:50%}
</style>
</head>
<body>
<svg width="0" height="0" style="position:absolute">
  <symbol id="pin" viewBox="0 0 12 16"><path d="M6 0a6 6 0 0 0-6 6c0 4.5 6 10 6 10s6-5.5 6-10a6 6 0 0 0-6-6z"/><circle cx="6" cy="6" r="2.3" fill="#fff"/></symbol>
  <symbol id="tick" viewBox="0 0 14 14"><circle cx="7" cy="7" r="6" fill="none" stroke="currentColor" stroke-width="1.3"/><path d="M4 7.2l2 2 4-4" fill="none" stroke="currentColor" stroke-width="1.3"/></symbol>
  <symbol id="div" viewBox="0 0 80 14"><line x1="0" y1="7" x2="30" y2="7" stroke="#f7a52b" stroke-width="2"/><line x1="50" y1="7" x2="80" y2="7" stroke="#f7a52b" stroke-width="2"/><circle cx="40" cy="7" r="6" fill="none" stroke="#7dc242" stroke-width="1.5"/><circle cx="40" cy="7" r="3" fill="#7dc242"/></symbol>
</svg>

<header>
  <div class="logo" style="left:141px;top:22px">
    <div class="mark"></div>
    <div class="name">QUILLBY<br>TREE CARE</div>
  </div>
  <a class="nav" style="left:583px">Home</a>
  <a class="nav" style="left:667px">About Us</a>
  <a class="nav" style="left:771px">Services</a>
  <a class="nav" style="left:873px">Blog</a>
  <a class="btn" style="left:946px;top:32px;width:113px;height:33px">Contact Us</a>
</header>

<section class="hero">
  <div class="photo" role="img" aria-label="Arborist in safety gear climbing a tall tree with a chainsaw against a clear blue sky" style="inset:0;background:linear-gradient(100deg,#1a66b8 0%,#2278cc 45%,#2b5f8e 70%,#4a4030 100%)"></div>
  <svg class="abs" style="left:0;bottom:0" width="1200" height="140" viewBox="0 0 1200 140">
    <path d="M0 110 C250 40 500 60 750 80 S1050 80 1200 0 L1200 140 L0 140Z" fill="#fff"/>
    <path d="M0 110 C250 40 500 60 750 80 S1050 80 1200 0 L1200 12 C1050 92 900 95 750 95 S250 55 0 118Z" fill="var(--orange)"/>
  </svg>
  <h1>EXPERT TREE CARE<br>AND &nbsp;LANDSCAPING<br>SOLUTIONS FOR YOU</h1>
  <p>Serving Lafayette &amp; Surrounding Areas.</p>
  <a class="btn" style="left:141px;top:327px;width:113px;height:34px">Contact Us</a>
</section>

<section>
  <h2 class="title abs" style="left:0;width:1200px;text-align:center;top:736px">OUR SERVICES</h2>
  <svg class="divider" style="left:560px;top:785px"><use href="#div"/></svg>
  <p class="abs" style="left:260px;width:680px;top:816px;text-align:center;font-size:15.5px;line-height:28px;color:#333">Lorem Ipsum is simply dummy text of the printing and typesetting industry. Lorem Ipsum has been the industry's standard dummy text ever since.</p>
  <svg class="arrow" style="left:84px" viewBox="0 0 36 36"><circle cx="18" cy="18" r="16" fill="none" stroke="#f7a52b" stroke-width="1.5"/><path d="M24 18H12m5-5l-5 5 5 5" fill="none" stroke="#f7a52b" stroke-width="1.5"/></svg>
  <svg class="arrow" style="left:1080px" viewBox="0 0 36 36"><circle cx="18" cy="18" r="17" fill="#f7a52b"/><path d="M12 18h12m-5-5l5 5-5 5" fill="none" stroke="#222" stroke-width="1.6"/></svg>

  <div class="svc" style="left:141px"><div class="img" role="img" aria-label="Gloved hands pruning a branch with shears" style="background:linear-gradient(135deg,#3f7a1e,#8bbf3f)"></div><h3>Tree Pruning</h3><a>Learn More</a></div>
  <div class="svc active" style="left:375px"><div class="img" role="img" aria-label="Worker cutting a log with a chainsaw" style="background:linear-gradient(135deg,#4d6b2e,#8a6a45)"></div><h3>Tree Removal</h3><p>Lorem Ipsum is simply dummy text of the printing and typesetting industry.</p><a>Learn More</a></div>
  <div class="svc" style="left:611px"><div class="img" role="img" aria-label="Crew member in hi-vis vest tending young trees" style="background:linear-gradient(135deg,#5b6e3c,#c67a3a)"></div><h3>Tree Preservation</h3><a>Learn More</a></div>
  <div class="svc" style="left:847px"><div class="img" role="img" aria-label="Stump grinder working on a tree stump" style="background:linear-gradient(135deg,#7a5a3a,#d6a24a)"></div><h3>Stump Grinding</h3><a>Learn More</a></div>
  <a class="btn" style="left:530px;top:1275px;width:141px;height:35px">View All Services</a>
</section>

<section>
  <div class="photo" role="img" aria-label="Person starting a chainsaw on a tree stump in a pine forest" style="left:0;top:1395px;width:1200px;height:593px;background:linear-gradient(90deg,#3b3a2c,#6a5a3c 35%,#55603e 65%,#6b7a5a)"></div>
  <div class="panel" style="left:608px;top:1479px;width:451px;height:422px;padding:40px 32px">
    <h2>ABOUT QUILLBY<br>TREE CARE</h2>
    <svg width="80" height="14" style="display:block;margin:6px 0 16px"><use href="#div"/></svg>
    <p>At Quillby Tree Care, we are more than just a tree service company, we are stewards of our beautiful trees. With a passion deeply rooted in arboriculture, we embark on a mission to promote the health, beauty, and safety of your trees and landscapes.</p>
    <p style="margin-top:10px">Whether it's expert tree trimming to enhance aesthetics, meticulous tree removal to mitigate hazards, or comprehensive tree health assessments to ensure safety, we approach each task with unwavering dedication and attention to detail.</p>
    <a class="btn orange inline" style="margin-top:16px;width:107px;height:34px">Contact Us</a>
  </div>
</section>

<section>
  <div class="photo" role="img" aria-label="Outline map of the service region with location pins, Scott marked at centre" style="left:143px;top:2072px;width:413px;height:436px;background:radial-gradient(ellipse at center,#eef3ea 0%,#f7f9f5 60%,#fff 75%)"></div>
  <h2 class="title abs" style="left:697px;top:2122px">SERVICE AREA</h2>
  <svg class="divider" style="left:697px;top:2172px"><use href="#div"/></svg>
  <ul class="area-list" style="left:697px;top:2198px">
    <li><svg width="12" height="16" fill="#f7a52b"><use href="#pin"/></svg>Carencro</li>
    <li style="font-weight:700"><svg width="12" height="16" fill="#7dc242"><use href="#pin"/></svg>Scott</li>
    <li><svg width="12" height="16" fill="#f7a52b"><use href="#pin"/></svg>Judice</li>
    <li><svg width="12" height="16" fill="#f7a52b"><use href="#pin"/></svg>Morgan City</li>
    <li><svg width="12" height="16" fill="#f7a52b"><use href="#pin"/></svg>Denham Spring</li>
  </ul>
  <ul class="area-list" style="left:868px;top:2198px">
    <li><svg width="12" height="16" fill="#f7a52b"><use href="#pin"/></svg>Duson</li>
    <li><svg width="12" height="16" fill="#f7a52b"><use href="#pin"/></svg>Broussard</li>
    <li><svg width="12" height="16" fill="#f7a52b"><use href="#pin"/></svg>Youngsville</li>
    <li><svg width="12" height="16" fill="#f7a52b"><use href="#pin"/></svg>Shenandoah</li>
    <li><svg width="12" height="16" fill="#f7a52b"><use href="#pin"/></svg>Lake Charles</li>
  </ul>
  <a class="btn" style="left:697px;top:2415px;width:107px;height:34px">Contact Us</a>
</section>

<section>
  <div class="photo" role="img" aria-label="Arborist in a bucket lift trimming branches beside a house" style="left:0;top:2592px;width:1200px;height:524px;background:linear-gradient(90deg,#5b6a4a,#3f5a2a 45%,#4e7a32 70%,#6b8a4a)"></div>
  <div class="panel" style="left:141px;top:2677px;width:452px;height:353px;padding:38px 24px">
    <h2 style="font-size:26px">WHY CHOOSE US?</h2>
    <svg width="80" height="14" style="display:block;margin-top:4px"><use href="#div"/></svg>
    <div class="why-grid">
      <div class="why-list" style="width:243px">
        <span><svg width="14" height="14" style="color:var(--orange)"><use href="#tick"/></svg>Locally Owned &amp; Operated</span>
        <span><svg width="14" height="14" style="color:var(--orange)"><use href="#tick"/></svg>Safety is Our No.1 Priority</span>
        <span><svg width="14" height="14" style="color:var(--orange)"><use href="#tick"/></svg>Licensed Arborist on Staff</span>
        <span><svg width="14" height="14" style="color:var(--orange)"><use href="#tick"/></svg>24-Hours Emergency Services</span>
      </div>
      <div class="why-list">
        <span><svg width="14" height="14" style="color:var(--orange)"><use href="#tick"/></svg>Licensed &amp; Insured</span>
        <span><svg width="14" height="14" style="color:var(--orange)"><use href="#tick"/></svg>Professional Work</span>
        <span><svg width="14" height="14" style="color:var(--orange)"><use href="#tick"/></svg>Free Estimates</span>
      </div>
    </div>
    <a class="btn orange inline" style="margin-top:16px;width:125px;height:40px;font-size:15px">Contact Us</a>
  </div>
</section>

<section>
  <h2 class="title abs" style="left:0;width:1200px;text-align:center;top:3193px">LATEST BLOG POSTS</h2>
  <svg class="divider" style="left:560px;top:3242px"><use href="#div"/></svg>

  <article class="blog" style="left:141px;top:3287px;width:500px;height:225px">
    <div class="abs" role="img" aria-label="Chainsaw cutting through a log with sawdust flying" style="left:0;top:0;width:208px;height:225px;background:linear-gradient(135deg,#6a5030,#c89050)"></div>
    <div class="abs" style="left:238px;top:42px;width:250px">
      <div class="date"><svg width="14" height="14" fill="#7dc242"><rect x="1" y="3" width="12" height="10" rx="1"/></svg>12.06.2024</div>
      <h3>Dolor Sit Amet Lorem Ipsum Ctetuer Conse Adipis.</h3>
      <p>Lorem ipsum dolor sit amet consectetuer adipiscing elit, sed diam nonummy nibh euismod tincidunt ut laoreet...</p>
    </div>
  </article>
  <article class="blog" style="left:141px;top:3541px;width:500px;height:225px">
    <div class="abs" role="img" aria-label="Felled tree branches lying on grass" style="left:0;top:0;width:208px;height:225px;background:linear-gradient(135deg,#4a6a2a,#8aa060)"></div>
    <div class="abs" style="left:238px;top:42px;width:250px">
      <div class="date"><svg width="14" height="14" fill="#7dc242"><rect x="1" y="3" width="12" height="10" rx="1"/></svg>11.06.2024</div>
      <h3>Lorem Ipsum Dolor Sit Amet Conse Ctetuer Adipis.</h3>
      <p>Lorem ipsum dolor sit amet consectetuer adipiscing elit, sed diam nonummy nibh euismod tincidunt ut laoreet...</p>
    </div>
  </article>
  <article class="blog" style="left:663px;top:3287px;width:396px;height:479px">
    <div class="abs" role="img" aria-label="Arborist in a helmet climbing among tree branches" style="left:0;top:0;width:396px;height:247px;background:linear-gradient(135deg,#3e5a2a,#8a9a6a)"></div>
    <div class="abs" style="left:25px;top:275px;width:350px">
      <div class="date"><svg width="14" height="14" fill="#f7a52b"><rect x="1" y="3" width="12" height="10" rx="1"/></svg>10.12.2017</div>
      <h3>Dolor Sit Amet Lorem Ipsum Ctetuer Conse Adipis Dolor Ipsum.</h3>
      <p>Lorem ipsum dolor sit amet, consectetur adipiscing elit. Fusce ac quam sit amet massa feugiat tincidunt eu nec libero. Duis id libero sem. Quisque vestibulum feugiat odio, at egestas velit lacinia mattis...</p>
    </div>
  </article>
  <a class="btn" style="left:535px;top:3796px;width:128px;height:35px">View All Blogs</a>
</section>

<section>
  <div class="photo" role="img" aria-label="Faded view looking up into a green tree canopy" style="left:0;top:3917px;width:1200px;height:600px;background:linear-gradient(180deg,#dfe6d6,#eef2e8 50%,#e6ebdd)"></div>
  <h2 class="title abs" style="left:141px;top:3997px">CONTACT US</h2>
  <svg class="divider" style="left:141px;top:4046px"><use href="#div"/></svg>
  <h2 class="title abs" style="left:680px;top:3997px">QUICK INQUIRY</h2>
  <svg class="divider" style="left:680px;top:4046px"><use href="#div"/></svg>

  <div class="photo" role="img" aria-label="Smiling arborist wearing a yellow hard hat in front of trees" style="left:141px;top:4093px;width:314px;height:314px;border-radius:0 0 16px 0;background:linear-gradient(135deg,#c9a020,#4a6a2a 60%,#2a3e5a)"></div>
  <div class="abs" style="left:364px;top:4110px;width:264px;height:280px;background:#fff;border-radius:10px;box-shadow:0 2px 10px rgba(0,0,0,.12);padding:22px 20px;font-size:12px;line-height:17px">
    <div style="font-weight:600;font-size:13px;margin-bottom:16px">Free Estimate From MARLOWE</div>
    <div style="display:flex;gap:14px;margin-bottom:18px"><svg width="26" height="26" viewBox="0 0 26 26" fill="none" stroke="#7dc242" stroke-width="1.5"><path d="M13 3a7 7 0 0 0-7 7c0 5 7 12 7 12s7-7 7-12a7 7 0 0 0-7-7z"/><circle cx="13" cy="10" r="2.5"/></svg><span>123, Building Name, Street<br>Lafayette, Louisiana.</span></div>
    <div style="display:flex;gap:14px;margin-bottom:18px"><svg width="26" height="26" viewBox="0 0 26 26" fill="none" stroke="#7dc242" stroke-width="1.5"><path d="M6 4l4 0 2 5-3 2c1 3 3 5 6 6l2-3 5 2 0 4c-9 1-17-7-16-16z"/></svg><span>(337) 555-0148<br>(318) 555-0192</span></div>
    <div style="display:flex;gap:14px;margin-bottom:18px"><svg width="26" height="26" viewBox="0 0 26 26" fill="none" stroke="#7dc242" stroke-width="1.5"><rect x="3" y="7" width="20" height="14"/><path d="M3 7l10 8 10-8"/></svg><span>E-Mail<br>info@quillbytreecare.com</span></div>
    <div style="display:flex;gap:14px"><svg width="26" height="26" viewBox="0 0 26 26" fill="none" stroke="#7dc242" stroke-width="1.5"><circle cx="13" cy="13" r="10"/><path d="M13 7v6l4 3"/></svg><span><b>Reachable for You</b><br>Mo. - Fr. : 8:00 AM - 5.00 PM</span></div>
  </div>

  <div class="field" style="top:4093px;height:41px">Name</div>
  <div class="field" style="top:4142px;height:41px">Email</div>
  <div class="field" style="top:4192px;height:41px">Phone</div>
  <div class="field" style="top:4242px;height:72px">Message</div>
  <a class="btn" style="left:689px;top:4337px;width:108px;height:35px">Submit Now</a>
</section>

<footer>
  <svg class="abs" style="left:0;top:4440px" width="1200" height="345" viewBox="0 0 1200 345">
    <path d="M0 120 C300 10 900 10 1200 120 L1200 345 L0 345Z" fill="var(--orange)"/>
    <path d="M0 130 C300 22 900 22 1200 130 L1200 345 L0 345Z" fill="var(--dark)"/>
  </svg>
  <div class="logo" style="left:466px;top:4530px">
    <div class="mark" style="width:40px;height:40px;background:#fff"></div>
    <div class="name" style="color:#fff;font-size:24px;letter-spacing:2px">QUILLBY<br>TREE CARE</div>
  </div>
  <a class="footnav" style="left:371px">Home</a>
  <a class="footnav" style="left:459px">About Us</a>
  <a class="footnav" style="left:569px">Services</a>
  <a class="footnav" style="left:675px">Blog</a>
  <a class="footnav" style="left:753px">Contact Us</a>
  <div class="abs" style="left:141px;top:4718px;width:918px;height:1px;background:#4a5557"></div>
  <p class="abs" style="left:141px;top:4745px;font-size:11px;color:#ddd">© 2024 Quillby Tree Care. All Rights Reserved.</p>
  <span class="social" style="left:947px"></span>
  <span class="social" style="left:986px"></span>
  <span class="social" style="left:1026px"></span>
</footer>
</body>
</html>
```